Larkspur Ridge Management - Business Cards

I need business cards. My current logo was designed by a designer at this site and I very much like and am happy with the results. I would like a business card that is trendy, unique, current yet professional. I deal with high net worth clients daily

Target Market(s)

Out of state investors looking to get into the rental market in Ohio

Industry/Entity Type

Property Management, Consulting

Contact Information for Business Card

Name, Title (Chief Financial Officer) office phone number (555) 817-3094 website address larkridgemgmt.example

Font styles to use
Sans Serif

Colors
0054AA
0677BA
7BADD7
CADEEF
E8F1F8
0094D4
00A9DD
6FCCEA
C7EBF8
E9F6FB
00AB8E
00BBA5
67D7C9
C6EFE9
E9F9F6

```html
<!DOCTYPE html>
<html lang="en">
<head>
<meta charset="utf-8">
<title>Larkspur Ridge Management – Business Cards</title>
<link href="https://fonts.googleapis.com/css2?family=Montserrat:wght@400;500;700&display=swap" rel="stylesheet">
<style>
  :root {
    --bg: #f1f1f1;
    --card: #ffffff;
    --navy: #253a66;
    --rule: #c3c8d4;
    --shadow: rgba(0, 0, 0, 0.08);
  }
  * { box-sizing: border-box; margin: 0; padding: 0; }
  html, body {
    width: 1200px; height: 1200px; overflow: hidden;
    background: var(--bg);
    font-family: "Montserrat", sans-serif;
    color: var(--navy);
  }
  .card {
    position: absolute;
    left: 223px; width: 755px; height: 431px;
    background: var(--card);
    box-shadow: 0 2px 10px var(--shadow);
  }
  .card--front { top: 101px; }
  .card--back { top: 667px; }

  .brand {
    position: absolute;
    display: flex; align-items: center; gap: 12px;
    color: var(--navy);
    font-weight: 700;
    text-transform: uppercase;
  }
  .brand__mark { background: var(--navy); flex: none; }
  .brand__name { line-height: 1.15; letter-spacing: 0.04em; }

  .card--front .brand { left: 78px; top: 136px; width: 240px; }
  .card--front .brand__mark { width: 22px; height: 22px; }
  .card--front .brand__name { font-size: 17px; }

  .card--back .brand {
    left: 0; right: 0; top: 168px;
    justify-content: center;
  }
  .card--back .brand__mark { width: 30px; height: 30px; }
  .card--back .brand__name { font-size: 24px; text-align: left; }

  .identity { position: absolute; left: 489px; top: 76px; }
  .identity__name {
    font-size: 24px; font-weight: 700; letter-spacing: 0.1em; line-height: 1;
  }
  .identity__title {
    font-size: 15px; font-weight: 500; letter-spacing: 0.04em; margin-top: 6px;
  }
  .contact { list-style: none; margin-top: 44px; }
  .contact__item {
    display: flex; align-items: center; gap: 14px;
    font-size: 12.5px; font-weight: 500; letter-spacing: 0.1em;
    height: 23px;
  }
  .icon { width: 13px; height: 13px; flex: none; }

  .web-line {
    position: absolute; left: 0; right: 0; top: 348px;
    display: flex; align-items: center; justify-content: center; gap: 16px;
    font-size: 13px; font-weight: 500; letter-spacing: 0.12em;
  }
  .web-line__rule { width: 36px; height: 1px; background: var(--rule); }
  .web-line .icon { width: 18px; height: 18px; }
</style>
</head>
<body>

<section class="card card--front">
  <div class="brand">
    <span class="brand__mark"></span>
    <span class="brand__name">Larkspur Ridge Management</span>
  </div>
  <div class="identity">
    <h1 class="identity__name">JOHN DOE</h1>
    <p class="identity__title">Chief Financial Officer</p>
    <ul class="contact">
      <li class="contact__item">
        <svg class="icon" viewBox="0 0 24 24" fill="none" stroke="currentColor" stroke-width="2" stroke-linejoin="round"><path d="M5 3h4l2 5-2.5 1.5a11 11 0 0 0 6 6L16 13l5 2v4a2 2 0 0 1-2 2A16 16 0 0 1 3 5a2 2 0 0 1 2-2z"/></svg>
        <span>(555) 817-3094</span>
      </li>
      <li class="contact__item">
        <svg class="icon" viewBox="0 0 24 24" fill="none" stroke="currentColor" stroke-width="2"><circle cx="12" cy="12" r="10"/><path d="M2 12h20M12 2a15 15 0 0 1 0 20M12 2a15 15 0 0 0 0 20"/></svg>
        <span>larkridgemgmt.example</span>
      </li>
    </ul>
  </div>
</section>

<section class="card card--back">
  <div class="brand">
    <span class="brand__mark"></span>
    <span class="brand__name">Larkspur Ridge<br>Management</span>
  </div>
  <div class="web-line">
    <span class="web-line__rule"></span>
    <svg class="icon" viewBox="0 0 24 24" fill="none" stroke="currentColor" stroke-width="1.8"><circle cx="12" cy="12" r="10"/><path d="M2 12h20M12 2a15 15 0 0 1 0 20M12 2a15 15 0 0 0 0 20"/></svg>
    <span>larkridgemgmt.example</span>
    <span class="web-line__rule"></span>
  </div>
</section>

</body>
</html>
```